Verdalunex webpage design

We are offering eco/sustainable theme vacations and make them bookable via our site. Our reference site is www.hovkalume.com. We want something similar but with a bit more creativity and elegant design. In our colors, which would depend on our logo colors.

NB: WE ARE NOT ASKING FOR A FULL BLOWN SITE. WE NEED 2 PAGE DESIGN FOR THE FIRST IMPRESSION. AFTER THAT WE CREATE A BUDGET FOR COMPLETION OF THE PROJECT.

Target Market(s)

Eco/Sustainable tourism.

Industry/Entity Type

Tourism

Coding

Coded - Design and coding required

Number of Pages Required

2 page

Requirements
Must have
• Reference site is hovkalume.com. But be creative and design something a bit different and more beautiful.
• NB: WE ARE NOT ASKING FOR A FULL BLOWN SITE. WE NEED 2 PAGE DESIGN FOR THE FIRST IMPRESSION. AFTER THAT WE CREATE A BUDGET FOR COMPLETION OF THE PROJECT.
• Please see our logo.

```html
<!DOCTYPE html>
<html lang="en">
<head>
<meta charset="utf-8">
<title>Verdalunex — Travel With Us</title>
<link href="https://fonts.googleapis.com/css2?family=Abel&family=Damion&family=Poppins:wght@300;400;500;600&display=swap" rel="stylesheet">
<style>
:root{
  --orange:#f47b20;
  --sky:#27b3ef;
  --price:#1ba3e0;
  --ink:#222;
  --text:#555;
  --line:#e6e6e6;
  --panel:#f3f3f3;
  --footer:#242424;
  --footer-bottom:#1b1b1b;
  --white:#fff;
}
*{box-sizing:border-box;margin:0;padding:0}
html,body{width:1200px;height:2525px;overflow:hidden}
body{position:relative;background:var(--white);font-family:'Poppins',sans-serif;color:var(--text)}
.abs{position:absolute}

/* hero */
.hero{left:0;top:0;width:1200px;height:540px;background:linear-gradient(180deg,#e9e2dc 0%,#9cc0d6 50%,#3f86b3 100%)}
.hero-wave{left:0;top:470px;width:1200px;height:90px}
.brand{left:112px;top:22px;display:flex;align-items:center;gap:10px;font-weight:600;font-size:22px;color:#1b3d6b}
.brand-dot{width:18px;height:18px;border-radius:50%;background:var(--orange)}
.top-nav{left:908px;top:31px;display:flex;gap:22px;font-size:12px;color:#222;align-items:center}
.top-nav span{display:flex;align-items:center;gap:5px}
.wish{left:1052px;top:22px;width:30px;height:30px;border-radius:50%;background:var(--price);display:flex;align-items:center;justify-content:center}
.wish-count{left:1078px;top:16px;font-size:10px;color:#555}
.hero-title{left:202px;top:232px;font-family:'Damion',cursive;font-weight:400;font-size:70px;color:#151515;line-height:1;white-space:nowrap}
.hero-sub{left:392px;top:322px;font-family:'Damion',cursive;font-size:54px;color:#151515;line-height:1;white-space:nowrap}

.plan{left:779px;top:131px;width:307px;height:354px;background:rgba(255,255,255,.94);box-shadow:0 4px 18px rgba(0,0,0,.18)}
.plan-head{left:7px;top:10px;width:291px;height:56px;background:var(--orange);color:#fff;font-family:'Damion',cursive;font-size:34px;text-align:center;line-height:56px}
.plan-field{left:31px;width:244px;height:39px;background:#fff;border:1px solid var(--line);font-size:12px;color:#888;display:flex;align-items:center;padding:0 12px;gap:8px}
.plan-field::after{content:"";margin-left:auto;border:5px solid transparent;border-top:6px solid #aaa;margin-top:5px}
.plan-btn{left:31px;top:266px;width:244px;height:39px;background:var(--orange);color:#fff;font-size:12px;font-weight:600;text-align:center;line-height:39px;letter-spacing:.5px}

/* steps band */
.steps{left:111px;top:522px;width:976px;height:185px;background:var(--sky);display:flex}
.step{flex:1;display:flex;flex-direction:column;align-items:center;justify-content:center;gap:10px;color:#fff;font-size:14px}

/* sidebar */
.sidebar{left:111px;top:751px;width:258px;height:1176px;background:var(--panel)}
.side-head{position:absolute;left:8px;width:250px;display:flex;align-items:center;gap:10px;font-family:'Abel',sans-serif;font-weight:400;font-size:22px;color:#222;padding-bottom:6px;border-bottom:2px solid var(--orange)}
.side-list{position:absolute;left:8px;width:240px;list-style:none}
.side-list li{height:25.3px;display:flex;align-items:center;font-size:11px;color:#444;white-space:nowrap}
.side-list li::before{content:"»";color:#aaa;margin-right:9px;font-size:11px}
.side-list li .plus{margin-left:auto;color:#555;font-size:13px}
.side-list li .box{margin-left:auto;width:9px;height:9px;border:1px solid #ccc;border-radius:2px;background:#fff}
.date-btn{left:8px;top:1009px;width:140px;height:22px;border-radius:11px;background:#fff;color:var(--orange);font-size:10px;display:flex;align-items:center;justify-content:center}

/* listing toolbar */
.sort{left:400px;top:754px;width:164px;height:37px;background:#f6f6f6;font-size:12px;color:#555;display:flex;align-items:center;padding-left:26px}
.sort::after{content:"";position:absolute;right:14px;top:15px;border:5px solid transparent;border-top:6px solid #aaa}
.view-toggle{left:580px;top:754px;width:102px;height:37px;background:#f6f6f6;display:flex;align-items:center;justify-content:center;gap:16px}
.filters{left:394px;top:808px;width:695px;height:84px;background:#f7f7f7}
.filters-label{left:11px;top:14px;font-size:12px;color:#444}
.chips{left:11px;top:41px;display:flex;gap:13px}
.chip{height:26px;padding:0 12px;background:#fff;border-radius:13px;font-size:11px;color:#444;display:flex;align-items:center;gap:14px}
.chip::after{content:"×";color:#bbb;font-size:13px}

/* tour cards */
.card{left:394px;width:695px;height:242px;background:#fff;box-shadow:0 1px 6px rgba(0,0,0,.08)}
.card-photo{left:0;top:0;width:241px;height:242px}
.photo-harbour{background:linear-gradient(180deg,#8fc6e4 0%,#2a96ad 100%)}
.photo-castle{background:linear-gradient(180deg,#b8d2e6 0%,#5f8f4a 100%)}
.fav{left:199px;top:10px;width:30px;height:30px;border-radius:50%;background:#fff;display:flex;align-items:center;justify-content:center}
.fav-plain{background:transparent}
.card-title{left:257px;top:16px;font-family:'Abel',sans-serif;font-weight:400;font-size:22px;color:#222;white-space:nowrap}
.card-meta{left:257px;top:49px;font-size:8.5px;letter-spacing:.5px;color:#bbb}
.card-feat{left:257px;font-size:11px;color:#666}
.card-feat::before{content:"";display:inline-block;width:5px;height:5px;border-radius:50%;border:1px solid #ccc;margin-right:8px;vertical-align:middle}
.rating{left:606px;top:26px;font-size:10px;color:#555}
.stars{left:606px;top:41px;font-size:14px;letter-spacing:1px;color:#1b3d6b}
.stars .off{color:#ccc}
.price-box{left:463px;top:87px;width:213px;height:138px;border:1px solid var(--line);border-radius:4px}
.price-inner{left:0;top:0;width:211px;height:66px;border-bottom:1px solid var(--line)}
.price-from{left:12px;top:12px;font-size:9px;color:#aaa}
.price-val{left:12px;top:26px;font-size:22px;color:var(--price);font-weight:500}
.price-for{left:12px;top:78px;font-size:10.5px;color:#333;font-weight:500}
.price-meta{left:12px;top:104px;display:flex;gap:18px;font-size:10px;color:#555;white-space:nowrap}
.price-meta span{display:flex;align-items:center;gap:5px}
.details-btn{left:257px;top:176px;width:147px;height:43px;border-radius:22px;background:var(--orange);color:#fff;font-size:13px;display:flex;align-items:center;justify-content:center}

/* footer */
.sea-fade{left:0;top:1930px;width:1200px;height:130px;background:linear-gradient(180deg,#fff 0%,#bfe4ec 100%)}
.footer-wave{left:0;top:2010px;width:1200px;height:70px}
.footer{left:0;top:2075px;width:1200px;height:383px;background:var(--footer)}
.footer-bottom{left:0;top:2458px;width:1200px;height:67px;background:var(--footer-bottom)}
.foot-head{font-size:21px;color:#fff;font-weight:500}
.foot-rule{height:1px;background:#3a3a3a}
.blog-thumb{width:76px;height:69px;background:linear-gradient(180deg,#e4e0da 0%,#cfc6bb 100%);border:2px solid #fff}
.blog-title{font-size:12px;color:#fff;white-space:nowrap}
.blog-date{font-size:11px;color:#bbb;font-style:italic}
.blog-text{font-size:10.5px;color:#999;line-height:1.9;width:320px}
.view-all{left:112px;top:2381px;font-size:11px;color:#fff;text-decoration:underline}
.quick-links{left:584px;top:2183px;list-style:none}
.quick-links li{height:29.8px;font-size:11px;color:#bbb}
.contact-icon{width:34px;height:34px;border:1px solid #444;display:flex;align-items:center;justify-content:center}
.contact-text{font-size:11px;color:#ccc;line-height:1.9;white-space:nowrap}
.contact-note{color:#999}
.social{width:34px;height:34px;border-radius:50%;background:var(--price)}
.copyright{left:111px;top:2483px;font-size:10.5px;color:#bbb}
.foot-brand{left:1022px;top:2479px;display:flex;align-items:center;gap:7px;font-size:14px;font-weight:600;color:#fff}
</style>
</head>
<body>

<!-- hero -->
<div class="abs hero" role="img" aria-label="Travellers resting on white cliffs above a calm blue sea"></div>
<svg class="abs hero-wave" viewBox="0 0 1200 90" preserveAspectRatio="none" aria-hidden="true">
  <path d="M0 40 C180 10 360 70 560 45 C760 20 900 5 1200 60 L1200 90 L0 90 Z" fill="#fff"/>
</svg>

<div class="abs brand"><span class="brand-dot"></span>Verdalunex</div>
<nav class="abs top-nav">
  <span><svg width="12" height="12" viewBox="0 0 12 12"><circle cx="6" cy="6" r="5.3" fill="none" stroke="#222"/><circle cx="6" cy="4.6" r="1.8" fill="#222"/><path d="M2.8 9.5c1-2 5.4-2 6.4 0" stroke="#222" fill="none"/></svg>Login</span>
  <span><svg width="12" height="12" viewBox="0 0 12 12"><path d="M2 10l1-3 5-5 2 2-5 5z" fill="none" stroke="#222"/></svg>Sign Up</span>
</nav>
<div class="abs wish"><svg width="14" height="13" viewBox="0 0 14 13"><path d="M7 12L1.5 6.5A3 3 0 0 1 7 2.4a3 3 0 0 1 5.5 4.1z" fill="#fff"/></svg></div>
<div class="abs wish-count">2</div>

<h1 class="abs hero-title">Travel With Us</h1>
<div class="abs hero-sub">For the best Deal</div>

<form class="abs plan">
  <div class="abs plan-head">Plan Your Trip</div>
  <div class="abs plan-field" style="top:96px"><svg width="10" height="13" viewBox="0 0 10 13"><path d="M5 12S1 7.5 1 5a4 4 0 0 1 8 0c0 2.5-4 7-4 7z" fill="none" stroke="#bbb"/></svg>Destination</div>
  <div class="abs plan-field" style="top:152px"><svg width="11" height="11" viewBox="0 0 11 11"><rect x=".5" y="1.5" width="10" height="9" fill="none" stroke="#bbb"/></svg>Select Duration or Date</div>
  <div class="abs plan-field" style="top:207px"><svg width="11" height="11" viewBox="0 0 11 11"><rect x=".5" y=".5" width="4" height="4" fill="none" stroke="#bbb"/><rect x="6.5" y=".5" width="4" height="4" fill="none" stroke="#bbb"/><rect x=".5" y="6.5" width="4" height="4" fill="none" stroke="#bbb"/><rect x="6.5" y="6.5" width="4" height="4" fill="none" stroke="#bbb"/></svg>Select Category</div>
  <div class="abs plan-btn">BOOK NOW</div>
</form>

<!-- steps -->
<section class="abs steps">
  <div class="step">
    <svg width="50" height="56" viewBox="0 0 50 56" fill="none" stroke="#fff" stroke-width="2"><circle cx="25" cy="16" r="14"/><circle cx="25" cy="13" r="5"/><path d="M16 25c4-6 14-6 18 0"/><rect x="5" y="38" width="40" height="12" rx="6"/><path d="M13 44h2M19 44h2M25 44h2M31 44h2"/></svg>
    <span>Login or Signup</span>
  </div>
  <div class="step">
    <svg width="64" height="56" viewBox="0 0 64 56" fill="none" stroke="#fff" stroke-width="2"><path d="M4 20l16-6 24 6 16-6v38l-16 6-24-6-16 6z"/><path d="M20 14v38M44 20v38"/><path d="M32 32S22 22 22 15a10 10 0 0 1 20 0c0 7-10 17-10 17z" fill="#27b3ef"/><circle cx="32" cy="15" r="4"/></svg>
    <span>Search and Discover</span>
  </div>
  <div class="step">
    <svg width="60" height="60" viewBox="0 0 60 60" fill="none" stroke="#fff" stroke-width="2"><rect x="4" y="8" width="46" height="40"/><path d="M4 18h46M14 4v8M40 4v8M12 26h6M24 26h6M36 26h6M12 34h6M24 34h6M12 42h6"/><circle cx="46" cy="46" r="10" fill="#27b3ef"/><path d="M46 41v10M41 46h10"/></svg>
    <span>Schedule Plan</span>
  </div>
  <div class="step">
    <svg width="60" height="56" viewBox="0 0 60 56" fill="none" stroke="#fff" stroke-width="2"><rect x="4" y="4" width="52" height="40" rx="3"/><path d="M4 13h52"/><circle cx="10" cy="8.5" r="1"/><circle cx="15" cy="8.5" r="1"/><path d="M26 22l8-4 10 10-10 14-10-8z"/><circle cx="34" cy="25" r="2"/></svg>
    <span>Get Quotation</span>
  </div>
</section>

<!-- sidebar -->
<aside class="abs sidebar">
  <h3 class="side-head" style="top:22px"><svg width="18" height="22" viewBox="0 0 18 22" fill="none" stroke="#f47b20" stroke-width="2"><circle cx="9" cy="7" r="5.5"/><path d="M2 20c1-5 13-5 14 0"/></svg>Destinations</h3>
  <ul class="side-list" style="top:65px">
    <li>Europe<span class="plus">+</span></li>
    <li>Asia &amp; Oceania<span class="plus">+</span></li>
    <li>Africa &amp; the Middle East<span class="plus">+</span></li>
    <li>The Americas &amp; Caribbean<span class="plus">+</span></li>
  </ul>

  <h3 class="side-head" style="top:196px"><svg width="22" height="22" viewBox="0 0 22 22" fill="#f47b20"><rect x="1" y="1" width="8" height="8"/><rect x="12" y="6" width="9" height="9"/><rect x="3" y="13" width="7" height="7"/></svg>Categories</h3>
  <ul class="side-list" style="top:239px">
    <li>Europe<span class="plus">+</span></li>
    <li>Asia &amp; Oceania<span class="plus">+</span></li>
    <li>Africa &amp; the Middle East<span class="plus">+</span></li>
    <li>The Americas &amp; Caribbean<span class="plus">+</span></li>
    <li>Europe<span class="plus">+</span></li>
    <li>Asia &amp; Oceania<span class="plus">+</span></li>
    <li>Africa &amp; the Middle East<span class="plus">+</span></li>
    <li>The Americas &amp; Caribbean<span class="plus">+</span></li>
    <li>Europe<span class="plus">+</span></li>
    <li>Asia &amp; Oceania<span class="plus">+</span></li>
    <li>Africa &amp; the Middle East<span class="plus">+</span></li>
    <li>The Americas &amp; Caribbean<span class="plus">+</span></li>
    <li>Europe<span class="plus">+</span></li>
    <li>Asia &amp; Oceania<span class="plus">+</span></li>
    <li>Africa &amp; the Middle East<span class="plus">+</span></li>
    <li>The Americas &amp; Caribbean<span class="plus">+</span></li>
  </ul>

  <h3 class="side-head" style="top:669px"><svg width="20" height="20" viewBox="0 0 20 20" fill="none" stroke="#f47b20" stroke-width="2"><ellipse cx="10" cy="5" rx="8" ry="3"/><path d="M2 5v10c0 1.7 3.6 3 8 3s8-1.3 8-3V5M2 10c0 1.7 3.6 3 8 3s8-1.3 8-3"/></svg>Price Per Trip</h3>
  <ul class="side-list" style="top:710px">
    <li>From US$0 to US$112<span class="box"></span></li>
    <li>From US$112 to US$337<span class="box"></span></li>
    <li>From US$337 to US$1,011<span class="box"></span></li>
    <li>More than US$1,011<span class="box"></span></li>
  </ul>

  <h3 class="side-head" style="top:845px"><svg width="20" height="20" viewBox="0 0 20 20" fill="none" stroke="#f47b20" stroke-width="2"><rect x="1" y="3" width="18" height="16"/><path d="M1 8h18M6 1v4M14 1v4"/></svg>Arrival Date</h3>
  <ul class="side-list" style="top:889px">
    <li>Europe<span class="box"></span></li>
    <li>Asia &amp; Oceania<span class="box"></span></li>
    <li>Africa &amp; the Middle East<span class="box"></span></li>
    <li>The Americas &amp; Caribbean<span class="box"></span></li>
  </ul>
  <div class="abs date-btn">Select Specific Date</div>
</aside>

<!-- toolbar -->
<div class="abs sort">Most Popular</div>
<div class="abs view-toggle">
  <svg width="18" height="18" viewBox="0 0 18 18" fill="#555"><rect width="8" height="8"/><rect x="10" width="8" height="8"/><rect y="10" width="8" height="8"/><rect x="10" y="10" width="8" height="8"/></svg>
  <svg width="20" height="18" viewBox="0 0 20 18" fill="#555"><rect width="3" height="3"/><rect x="6" y="0.5" width="14" height="2"/><rect y="7" width="3" height="3"/><rect x="6" y="7.5" width="14" height="2"/><rect y="14" width="3" height="3"/><rect x="6" y="14.5" width="14" height="2"/></svg>
</div>
<div class="abs filters">
  <div class="abs filters-label">Filtered By:</div>
  <div class="abs chips">
    <span class="chip">Europe</span><span class="chip">All Types</span><span class="chip">Europe</span><span class="chip">All Types</span><span class="chip">Europe</span>
  </div>
</div>

<!-- tour cards -->
<article class="abs card" style="top:912px">
  <div class="abs card-photo photo-harbour" role="img" aria-label="Harbour town with boats on turquoise water"></div>
  <div class="abs fav"><svg width="14" height="13" viewBox="0 0 14 13"><path d="M7 12L1.5 6.5A3 3 0 0 1 7 2.4a3 3 0 0 1 5.5 4.1z" fill="#f47b20"/></svg></div>
  <h2 class="abs card-title">Alpenhaus Nordwind</h2>
  <div class="abs card-meta">MIEMING › TIROL › AUSTRIA</div>
  <div class="abs card-feat" style="top:84px">Flexible Cancellation Policy</div>
  <div class="abs card-feat" style="top:103px">Airport Transfer Included</div>
  <div class="abs rating">2.5 k</div>
  <div class="abs stars">★★★<span class="off">★★</span></div>
  <div class="abs price-box"><div class="abs price-inner"></div><div class="abs price-from">From</div><div class="abs price-val">US $1,235</div><div class="abs price-for">Price For:</div><div class="abs price-meta"><span>👤 1 Person</span><span>▣ 6 days / 5 nights</span></div></div>
  <div class="abs details-btn">View Details</div>
</article>

<article class="abs card" style="top:1170px">
  <div class="abs card-photo photo-castle" role="img" aria-label="White hilltop castle above green forest"></div>
  <div class="abs fav fav-plain"><svg width="14" height="13" viewBox="0 0 14 13"><path d="M7 12L1.5 6.5A3 3 0 0 1 7 2.4a3 3 0 0 1 5.5 4.1z" fill="#f47b20"/></svg></div>
  <h2 class="abs card-title">Alpenhaus Nordwind</h2>
  <div class="abs card-meta">MIEMING › TIROL › AUSTRIA</div>
  <div class="abs card-feat" style="top:84px">Flexible Cancellation Policy</div>
  <div class="abs card-feat" style="top:103px">Airport Transfer Included</div>
  <div class="abs rating">2.5 k</div>
  <div class="abs stars">★★★<span class="off">★★</span></div>
  <div class="abs price-box"><div class="abs price-inner"></div><div class="abs price-from">From</div><div class="abs price-val">US $1,235</div><div class="abs price-for">Price For:</div><div class="abs price-meta"><span>👤 1 Person</span><span>▣ 6 days / 5 nights</span></div></div>
  <div class="abs details-btn">View Details</div>
</article>

<article class="abs card" style="top:1427px">
  <div class="abs card-photo photo-harbour" role="img" aria-label="Harbour town with boats on turquoise water"></div>
  <div class="abs fav"><svg width="14" height="13" viewBox="0 0 14 13"><path d="M7 12L1.5 6.5A3 3 0 0 1 7 2.4a3 3 0 0 1 5.5 4.1z" fill="#f47b20"/></svg></div>
  <h2 class="abs card-title">Alpenhaus Nordwind</h2>
  <div class="abs card-meta">MIEMING › TIROL › AUSTRIA</div>
  <div class="abs card-feat" style="top:84px">Flexible Cancellation Policy</div>
  <div class="abs card-feat" style="top:103px">Airport Transfer Included</div>
  <div class="abs rating">2.5 k</div>
  <div class="abs stars">★★★<span class="off">★★</span></div>
  <div class="abs price-box"><div class="abs price-inner"></div><div class="abs price-from">From</div><div class="abs price-val">US $1,235</div><div class="abs price-for">Price For:</div><div class="abs price-meta"><span>👤 1 Person</span><span>▣ 6 days / 5 nights</span></div></div>
  <div class="abs details-btn">View Details</div>
</article>

<article class="abs card" style="top:1685px">
  <div class="abs card-photo photo-castle" role="img" aria-label="White hilltop castle above green forest"></div>
  <div class="abs fav fav-plain"><svg width="14" height="13" viewBox="0 0 14 13"><path d="M7 12L1.5 6.5A3 3 0 0 1 7 2.4a3 3 0 0 1 5.5 4.1z" fill="#f47b20"/></svg></div>
  <h2 class="abs card-title">Alpenhaus Nordwind</h2>
  <div class="abs card-meta">MIEMING › TIROL › AUSTRIA</div>
  <div class="abs card-feat" style="top:84px">Flexible Cancellation Policy</div>
  <div class="abs card-feat" style="top:103px">Airport Transfer Included</div>
  <div class="abs rating">2.5 k</div>
  <div class="abs stars">★★★<span class="off">★★</span></div>
  <div class="abs price-box"><div class="abs price-inner"></div><div class="abs price-from">From</div><div class="abs price-val">US $1,235</div><div class="abs price-for">Price For:</div><div class="abs price-meta"><span>👤 1 Person</span><span>▣ 6 days / 5 nights</span></div></div>
  <div class="abs details-btn">View Details</div>
</article>

<!-- footer -->
<div class="abs sea-fade" role="img" aria-label="Soft sea water fading into the footer"></div>
<svg class="abs footer-wave" viewBox="0 0 1200 70" preserveAspectRatio="none" aria-hidden="true">
  <path d="M0 20 C150 5 260 45 420 38 C600 30 700 60 860 40 C1000 22 1100 10 1200 30 L1200 70 L0 70 Z" fill="#242424"/>
</svg>
<footer class="abs footer"></footer>

<h3 class="abs foot-head" style="left:111px;top:2127px">Latest Blog</h3>
<div class="abs foot-rule" style="left:111px;top:2165px;width:400px"></div>
<div class="abs blog-thumb" style="left:111px;top:2186px" role="img" aria-label="Blog author portrait"></div>
<div class="abs blog-title" style="left:204px;top:2181px">Lorem ipsum dolor sit amet</div>
<div class="abs blog-date" style="left:204px;top:2200px">June 9, 2014</div>
<p class="abs blog-text" style="left:204px;top:2222px">Contrary to popular belief, Lorem Ipsum is not sirandom text. It has roots in a piece of classical Latin.</p>
<div class="abs blog-thumb" style="left:111px;top:2297px" role="img" aria-label="Blog author portrait"></div>
<div class="abs blog-title" style="left:204px;top:2292px">Lorem ipsum dolor sit amet</div>
<div class="abs blog-date" style="left:204px;top:2311px">June 9, 2014</div>
<p class="abs blog-text" style="left:204px;top:2333px">Contrary to popular belief, Lorem Ipsum is not sirandom text. It has roots in a piece of classical Latin.</p>
<div class="abs view-all">VIEW ALL</div>

<h3 class="abs foot-head" style="left:584px;top:2127px">Quick Links</h3>
<div class="abs foot-rule" style="left:584px;top:2165px;width:160px"></div>
<ul class="abs quick-links">
  <li>Home</li><li>Menu Two</li><li>Menu Three</li><li>Menu Four</li><li>About Us</li><li>Book A Free Ticket</li><li>Why Choose Us</li><li>Get Help</li>
</ul>

<h3 class="abs foot-head" style="left:806px;top:2127px">Contact Us</h3>
<div class="abs foot-rule" style="left:806px;top:2165px;width:283px"></div>
<div class="abs contact-icon" style="left:806px;top:2186px"><svg width="14" height="14" viewBox="0 0 14 14"><path d="M3 1l2.5 3-1.5 1.5a8 8 0 0 0 4.5 4.5L10 8.5l3 2.5-1.5 2C6 13 1 8 1 2.5z" fill="#999"/></svg></div>
<div class="abs contact-text" style="left:858px;top:2181px">0147 82 3306 &nbsp;&nbsp;&nbsp;<span class="contact-note">(For urgent IT support)</span><br>0147 82 3306 &nbsp;&nbsp;&nbsp;<span class="contact-note">(For general inquiries)</span></div>
<div class="abs contact-icon" style="left:806px;top:2236px"><svg width="16" height="12" viewBox="0 0 16 12" fill="none" stroke="#999"><rect x=".5" y=".5" width="15" height="11"/><path d="M.5 .5L8 7l7.5-6.5"/></svg></div>
<div class="abs contact-text" style="left:858px;top:2242px">support@verdalunex.com</div>
<div class="abs contact-icon" style="left:806px;top:2287px"><svg width="12" height="15" viewBox="0 0 12 15"><path d="M6 14S1 8.5 1 5.5a5 5 0 0 1 10 0C11 8.5 6 14 6 14z" fill="#999"/><circle cx="6" cy="5.5" r="1.8" fill="#242424"/></svg></div>
<div class="abs contact-text" style="left:858px;top:2283px">Level 3, 17 Harbourline Road, Westcliff,<br>Marlow 0841</div>
<div class="abs social" style="left:806px;top:2358px" role="img" aria-label="Social network link"></div>
<div class="abs social" style="left:860px;top:2358px" role="img" aria-label="Social network link"></div>
<div class="abs social" style="left:912px;top:2358px" role="img" aria-label="Social network link"></div>

<div class="abs footer-bottom"></div>
<div class="abs copyright">© Copyright 2019 &nbsp;|&nbsp; All Rights Reserved</div>
<div class="abs foot-brand"><span class="brand-dot"></span>Verdalunex</div>

</body>
</html>
```